Business Card - Cooperate

Business Card for Larkfield Management Consulting

Target Market(s)

Corparte - b2B

Industry/Entity Type

Management Consulting - Professional Services

Contact Information for Business Card

Company Name , Slogan , Dummy Address,

Requirements
Must have
• Reach your Full Potential

```html
<!DOCTYPE html>
<html lang="en">
<head>
<meta charset="utf-8">
<title>Larkfield Management Consulting – Business Card</title>
<link rel="stylesheet" href="https://fonts.googleapis.com/css2?family=Montserrat:wght@300&family=Poppins:wght@400;600;700&display=swap">
<style>
  :root {
    --page-bg: #eeeef2;
    --navy: #19166f;
    --label-navy: #23207a;
    --brand-blue: #1f5fd6;
    --teal: #1ba39c;
    --white: #ffffff;
    --soft-blue: #cfe3fb;
    --soft-mint: #d7f2dc;
    --soft-lilac: #dcdcef;
  }
  * { margin: 0; padding: 0; box-sizing: border-box; }
  html, body {
    width: 1200px; height: 543px; overflow: hidden;
    background: var(--page-bg);
    font-family: "Poppins", sans-serif;
  }
  .canvas { position: relative; width: 1200px; height: 543px; }

  .side-label {
    position: absolute; top: 64px; width: 491px;
    font-family: "Montserrat", sans-serif; font-weight: 300;
    font-size: 26px; color: var(--label-navy);
    text-align: center; letter-spacing: 0.5px;
  }
  .side-label--front { left: 93px; }
  .side-label--back { left: 624px; }

  .card {
    position: absolute; top: 137px; width: 491px; height: 300px;
    overflow: hidden;
    box-shadow: 0 10px 30px rgba(30, 30, 60, 0.12);
  }
  .card--front { left: 93px; background: var(--white); }
  .card--back { left: 624px; background: var(--navy); }

  /* Front */
  .front-decor { position: absolute; left: 0; top: 0; width: 210px; height: 160px; }
  .brand-lockup { position: absolute; left: 136px; top: 76px; display: flex; align-items: center; gap: 20px; }
  .brand-dot { width: 36px; height: 36px; border-radius: 50%; background: var(--brand-blue); }
  .brand-name {
    font-weight: 600; font-size: 36px; line-height: 1;
    color: var(--brand-blue); letter-spacing: 0.5px;
  }
  .brand-slogan {
    position: absolute; left: 200px; top: 113px;
    font-weight: 700; font-size: 7.5px; color: var(--teal); letter-spacing: 1.3px;
  }
  .contact-band {
    position: absolute; left: 0; top: 197px; width: 100%; height: 103px;
    background: var(--navy); border-top-left-radius: 36px;
  }
  .contact-list { position: absolute; left: 35px; top: 13px; list-style: none; color: var(--white); font-size: 8px; }
  .contact-list li { height: 15.5px; }
  .contact-list li.contact-address { margin-top: 2px; }
  .band-ring { position: absolute; right: 0; top: 0; width: 95px; height: 103px; }

  /* Back */
  .back-mark {
    position: absolute; left: 50%; top: 60px; width: 88px; height: 88px;
    margin-left: -44px; border-radius: 50%; background: var(--white);
  }
  .back-name {
    position: absolute; left: 0; width: 100%; top: 166px;
    text-align: center; color: var(--white);
    font-weight: 600; font-size: 26px; line-height: 1; letter-spacing: 0.5px;
  }
  .back-slogan {
    position: absolute; left: 0; width: 100%; top: 200px;
    text-align: center; color: var(--white);
    font-weight: 700; font-size: 5.5px; letter-spacing: 0.8px;
  }
  .back-note {
    position: absolute; left: 40px; right: 40px; top: 257px;
    text-align: center; color: var(--white);
    font-size: 5.2px; line-height: 1.4; font-weight: 600;
  }
</style>
</head>
<body>
<main class="canvas">
  <h2 class="side-label side-label--front">FRONT DESIGN</h2>
  <h2 class="side-label side-label--back">BACK DESIGN</h2>

  <section class="card card--front" aria-label="Business card front">
    <svg class="front-decor" viewBox="0 0 210 160" role="img" aria-label="Soft blue and mint gradient decoration">
      <defs>
        <linearGradient id="decorGradient" x1="0" y1="0" x2="1" y2="1">
          <stop offset="0" stop-color="var(--soft-blue)"/>
          <stop offset="1" stop-color="var(--soft-mint)"/>
        </linearGradient>
      </defs>
      <circle cx="70" cy="8" r="45" fill="var(--soft-lilac)"/>
      <circle cx="50" cy="58" r="62" fill="url(#decorGradient)"/>
    </svg>

    <div class="brand-lockup">
      <span class="brand-dot" aria-hidden="true"></span>
      <span class="brand-name">larkfield</span>
    </div>
    <p class="brand-slogan">REACH YOUR FULL POTENTIAL</p>

    <div class="contact-band">
      <ul class="contact-list">
        <li>+10 555 XXX XXX</li>
        <li>hello@larkfield.com</li>
        <li>www.larkfield.com</li>
        <li class="contact-address">418 Cedar Row Street, Northgate District, Harlow 20417-5530, UK</li>
      </ul>
      <svg class="band-ring" viewBox="0 0 95 103" aria-hidden="true">
        <circle cx="90" cy="48" r="62" fill="none" stroke="var(--white)" stroke-width="10"/>
      </svg>
    </div>
  </section>

  <section class="card card--back" aria-label="Business card back">
    <span class="back-mark" aria-hidden="true"></span>
    <p class="back-name">larkfield</p>
    <p class="back-slogan">REACH YOUR FULL POTENTIAL</p>
    <p class="back-note">Larkfield Management Consulting partners with growing firms to sharpen strategy, strengthen teams and turn clear plans into steady, measurable results across every market we serve.<br>Practical advice, honest reviews and lasting support for leaders who aim to reach their full potential.</p>
  </section>
</main>
</body>
</html>
```